Business Card for a Wedding Films Business

We require a business card design for our business 'Lewis Marrow Wedding Films'. The logo needs to look classy and high end.

Target Market(s)

Wedding Couples

Contact Information for Business Card

Lewis Marrow Wedding Films
07312 605 227
films@lewismarrowreels.com
www.lewismarrowreels.com

Facebook: @lewismarrowweddingfilms
Instagram: @lewismarrowfilms

Font styles to use
Sans Serif

Requirements
Must have
• Social media icons - Facebook and Instagram

```html
<!DOCTYPE html>
<html lang="en">
<head>
<meta charset="utf-8">
<title>Lewis Marrow Wedding Films – Business Card</title>
<link href="https://fonts.googleapis.com/css2?family=Jost:wght@400;500&display=swap" rel="stylesheet">
<style>
  :root {
    --stage: #333333;
    --card-dark: #121212;
    --card-light: #ffffff;
    --ink-light: #ffffff;
    --ink-dark: #111111;
    --ink-muted: #5a5a5a;
    --deco-dark-a: #3a3a3a;
    --deco-dark-b: #6a6a6a;
    --deco-light-a: #8a8a8a;
    --deco-light-b: #3a3a3a;
  }
  * { margin: 0; padding: 0; box-sizing: border-box; }
  html, body {
    width: 1200px;
    height: 960px;
    overflow: hidden;
    background: var(--stage);
    font-family: "Jost", "Futura", sans-serif;
  }
  .canvas {
    position: relative;
    width: 1200px;
    height: 960px;
  }
  .card {
    position: absolute;
    top: 348px;
    width: 449px;
    height: 260px;
    overflow: hidden;
  }
  .card--front {
    left: 158px;
    background: var(--card-dark);
    color: var(--ink-light);
  }
  .card--back {
    left: 625px;
    background: var(--card-light);
    color: var(--ink-dark);
  }
  .monogram-area {
    position: absolute;
    top: 0;
    height: 260px;
  }
  .card--front .monogram-area {
    right: 0;
    width: 151px;
    background: linear-gradient(135deg, var(--deco-dark-a), var(--deco-dark-b));
  }
  .card--back .monogram-area {
    left: 0;
    width: 152px;
    background: linear-gradient(135deg, var(--deco-light-a), var(--deco-light-b));
  }
  .brand-dot {
    position: absolute;
    left: 161px;
    top: 86px;
    width: 40px;
    height: 40px;
    border-radius: 50%;
    background: var(--ink-light);
    transform: translateX(-50%);
  }
  .wordmark {
    position: absolute;
    text-align: center;
    white-space: nowrap;
    transform: translateX(-50%);
  }
  .card--front .wordmark { left: 161px; top: 149px; }
  .card--back .wordmark { left: 302px; top: 58px; }
  .wordmark__name {
    font-weight: 500;
    font-size: 23px;
    letter-spacing: 3.8px;
    line-height: 1;
  }
  .card--back .wordmark__name { font-size: 17.5px; letter-spacing: 3px; }
  .wordmark__tag {
    margin-top: 6px;
    font-weight: 500;
    font-size: 10.5px;
    letter-spacing: 4.4px;
    line-height: 1;
  }
  .card--back .wordmark__tag { font-size: 8px; letter-spacing: 3.3px; margin-top: 5px; }
  .contact {
    position: absolute;
    left: 218px;
    top: 108px;
    list-style: none;
  }
  .contact__item {
    display: flex;
    align-items: center;
    gap: 9px;
    height: 19px;
    font-size: 11.5px;
    color: var(--ink-muted);
  }
  .contact__item--gap { margin-top: 6px; }
  .contact__icon {
    width: 11px;
    height: 11px;
    flex: none;
    fill: var(--ink-dark);
  }
  .contact__mark {
    width: 10px;
    height: 10px;
    flex: none;
    background: var(--ink-dark);
    margin: 0 0.5px;
  }
  .contact__mark--round { border-radius: 50%; }
</style>
</head>
<body>
<main class="canvas">
  <section class="card card--front" aria-label="Card front">
    <div class="monogram-area" role="img" aria-label="Large brand monogram decoration, left half"></div>
    <span class="brand-dot" aria-hidden="true"></span>
    <div class="wordmark">
      <div class="wordmark__name">LEWIS MARROW</div>
      <div class="wordmark__tag">WEDDING FILMS</div>
    </div>
  </section>

  <section class="card card--back" aria-label="Card back">
    <div class="monogram-area" role="img" aria-label="Large brand monogram decoration, right half"></div>
    <div class="wordmark">
      <div class="wordmark__name">LEWIS MARROW</div>
      <div class="wordmark__tag">WEDDING FILMS</div>
    </div>
    <ul class="contact">
      <li class="contact__item">
        <svg class="contact__icon" viewBox="0 0 24 24" aria-hidden="true"><path d="M6.6 10.8a15.1 15.1 0 0 0 6.6 6.6l2.2-2.2a1 1 0 0 1 1-.25 11.4 11.4 0 0 0 3.6.57 1 1 0 0 1 1 1V20a1 1 0 0 1-1 1A17 17 0 0 1 3 4a1 1 0 0 1 1-1h3.5a1 1 0 0 1 1 1c0 1.25.2 2.45.57 3.6a1 1 0 0 1-.25 1z"/></svg>
        <span>07312 605 227</span>
      </li>
      <li class="contact__item">
        <svg class="contact__icon" viewBox="0 0 24 24" aria-hidden="true"><path d="M2 5h20v2l-10 6L2 7z"/><path d="M2 9.3l10 6 10-6V19H2z"/></svg>
        <span>films@lewismarrowreels.com</span>
      </li>
      <li class="contact__item">
        <svg class="contact__icon" viewBox="0 0 24 24" aria-hidden="true"><path d="M12 2a10 10 0 1 0 0 20 10 10 0 0 0 0-20zm6.9 6h-3a15.6 15.6 0 0 0-1.4-3.6A8 8 0 0 1 18.9 8zM12 4c.8 1.2 1.5 2.5 1.9 4h-3.8c.4-1.5 1.1-2.8 1.9-4zM4.3 14a8.2 8.2 0 0 1 0-4h3.4a16.5 16.5 0 0 0 0 4zm.8 2h3a15.6 15.6 0 0 0 1.4 3.6A8 8 0 0 1 5.1 16zm3-8h-3a8 8 0 0 1 4.4-3.6A15.6 15.6 0 0 0 8.1 8zM12 20c-.8-1.2-1.5-2.5-1.9-4h3.8c-.4 1.5-1.1 2.8-1.9 4zm2.3-6H9.7a14.7 14.7 0 0 1 0-4h4.6a14.7 14.7 0 0 1 0 4zm.2 5.6a15.6 15.6 0 0 0 1.4-3.6h3a8 8 0 0 1-4.4 3.6zm1.8-5.6a16.5 16.5 0 0 0 0-4h3.4a8.2 8.2 0 0 1 0 4z"/></svg>
        <span>www.lewismarrowreels.com</span>
      </li>
      <li class="contact__item contact__item--gap">
        <span class="contact__mark" aria-hidden="true"></span>
        <span>@lewismarrowweddingfilms</span>
      </li>
      <li class="contact__item">
        <span class="contact__mark contact__mark--round" aria-hidden="true"></span>
        <span>@lewismarrowfilms</span>
      </li>
    </ul>
  </section>
</main>
</body>
</html>
```